Brochure for Home Improvement Startup

We need an eye-catching, informative, and easy to read brochure design to help explain our services to our target audience which include baby boomers and seniors.

```html
<!DOCTYPE html>
<html lang="en">
<head>
<meta charset="utf-8">
<title>NestWell Solutions – Trifold Brochure</title>
<link href="https://fonts.googleapis.com/css2?family=Lato:wght@400;700&family=Roboto:wght@500;700&family=Roboto+Condensed:wght@700&display=swap" rel="stylesheet">
<style>
  :root {
    --magenta: #e0117f;
    --magenta-deep: #c40a6c;
    --ink: #111111;
    --charcoal: #4a4a4c;
    --paper: #ffffff;
    --paper-shade: #f1f1f1;
    --muted: #333333;
  }
  * { margin: 0; padding: 0; box-sizing: border-box; }
  html, body { width: 1200px; height: 1200px; overflow: hidden; background: var(--paper); }
  .canvas { position: relative; width: 1200px; height: 1200px; background: var(--paper); }

  .brochure {
    position: absolute; left: 70px; top: 201px; width: 1076px; height: 766px;
    background: var(--paper);
    box-shadow: 0 2px 8px rgba(0,0,0,0.25);
    overflow: hidden;
  }
  .panel { position: absolute; top: 0; height: 766px; overflow: hidden; }
  .panel--inside-flap { left: 0; width: 359px; background: linear-gradient(90deg, #fff 0%, #fff 85%, #f2f2f2 100%); }
  .panel--back { left: 359px; width: 368px; background: linear-gradient(90deg, #ececec 0%, #fff 15%, #fff 85%, #f0f0f0 100%); }
  .panel--cover { left: 727px; width: 349px; background: linear-gradient(90deg, #f0f0f0 0%, #fff 20%); }

  .abs { position: absolute; }

  /* Inside flap */
  .label { font-family: "Roboto", sans-serif; font-weight: 700; font-size: 14px; color: var(--magenta); letter-spacing: 0.2px; }
  .body-copy { font-family: "Lato", sans-serif; font-size: 12px; line-height: 15px; color: var(--muted); text-align: justify; }
  .mission-label { left: 30px; top: 69px; }
  .mission-copy { left: 30px; top: 87px; width: 307px; text-align: left; }
  .focus-label { left: 28px; top: 148px; }
  .focus-copy { left: 30px; top: 169px; width: 307px; position: absolute; z-index: 2; }
  .porch-fade { left: 20px; top: 235px; width: 320px; height: 90px; background: linear-gradient(180deg, rgba(235,235,235,0) 0%, rgba(228,228,228,0.8) 60%, rgba(240,240,240,0.4) 100%); }
  .chevron { left: 0; top: 280px; }

  .section-title { font-family: "Roboto", sans-serif; font-weight: 700; font-size: 26px; line-height: 33px; text-align: center; text-transform: uppercase; }
  .section-title .accent { color: var(--magenta); display: block; }
  .section-title .dark { color: var(--ink); display: block; }
  .services-title { left: 0; width: 359px; top: 407px; }
  .mansion-photo { left: 0; top: 484px; width: 359px; height: 238px; background: linear-gradient(180deg, #f4f4f4 0%, #cfcfcf 35%, #9c9c9c 70%, #c8c8c8 100%); }

  .footer-band { position: absolute; left: 0; right: 0; bottom: 0; height: 40px; background: linear-gradient(90deg, var(--magenta-deep), var(--magenta) 50%, var(--magenta-deep)); }
  .web { font-family: "Lato", sans-serif; font-size: 14px; letter-spacing: 2.4px; text-align: center; line-height: 40px; }
  .footer-band .web { color: var(--paper); }

  /* Back panel */
  .house-art { left: 0; top: 0; }
  .tagline { left: 0; width: 368px; top: 400px; font-family: "Roboto Condensed", sans-serif; font-weight: 700; font-size: 36px; line-height: 44px; text-align: center; text-transform: uppercase; }
  .tagline .accent { color: var(--magenta); display: block; }
  .tagline .dark { color: var(--ink); display: block; }
  .contact-mark { left: 157px; top: 532px; width: 52px; height: 52px; border-radius: 50%; border: 2px solid var(--ink); background: var(--paper); z-index: 2; }
  .contact-pill { left: 100px; top: 586px; width: 167px; height: 32px; border-radius: 16px; background: var(--magenta); color: var(--paper); font-family: "Roboto", sans-serif; font-weight: 500; font-size: 15px; line-height: 32px; text-align: center; }
  .address { left: 0; width: 368px; top: 629px; font-family: "Lato", sans-serif; font-size: 12.5px; line-height: 15px; color: var(--muted); text-align: center; text-transform: uppercase; }
  .phone { left: 0; width: 368px; top: 682px; font-family: "Roboto Condensed", sans-serif; font-weight: 700; font-size: 22px; color: var(--magenta); text-align: center; }
  .back-web { left: 0; width: 368px; bottom: 0; height: 40px; color: var(--ink); }

  /* Cover */
  .brand { left: 0; width: 349px; top: 70px; display: flex; align-items: center; justify-content: center; gap: 10px; }
  .brand-square { width: 18px; height: 18px; background: var(--magenta); }
  .brand-name { font-family: "Lato", sans-serif; font-weight: 700; font-size: 46px; color: var(--charcoal); }
  .cover-art { left: 0; top: 168px; }
  .cover-title { left: 0; top: 589px; width: 349px; height: 128px; background: linear-gradient(180deg, #2a2a2a 0%, #000 100%); text-align: center; padding-top: 26px; font-family: "Roboto", sans-serif; font-weight: 700; font-size: 36px; line-height: 42px; text-transform: uppercase; }
  .cover-title .accent { color: var(--magenta); display: block; }
  .cover-title .light { color: var(--paper); display: block; }
</style>
</head>
<body>
<div class="canvas">
  <div class="brochure">

    <!-- Inside flap -->
    <section class="panel panel--inside-flap">
      <h3 class="abs label mission-label">MISSION</h3>
      <p class="abs body-copy mission-copy">maintenance of our client’s homes to enhance their over-all quality of life.</p>
      <h3 class="abs label focus-label">FOCUS</h3>
      <div class="abs porch-fade" role="img" aria-label="Faded photo of a house porch with white railing"></div>
      <p class="body-copy focus-copy">We deliver light home modification service to seniors and boomers so their homes continue to meet their changing needs. Specifically, we provide consultation and aging in place assessments to homeowners, sales, and installation of high quality grab bars, threshold ramps, lighting, and smart home technology as well ongoing home maintenance through a home “Fitness Plan”.</p>
      <svg class="abs chevron" width="359" height="120" viewBox="0 0 359 120">
        <polygon points="0,0 180,93 359,0 359,18 180,111 0,18" fill="#111111"/>
      </svg>
      <h2 class="abs section-title services-title"><span class="accent">Home Assessments</span><span class="dark">and Consulting</span></h2>
      <div class="abs mansion-photo" role="img" aria-label="Black and white photo of a large Victorian house"></div>
      <div class="footer-band"><p class="web">www.nestwellsolutions.com</p></div>
    </section>

    <!-- Back panel -->
    <section class="panel panel--back">
      <svg class="abs house-art" width="368" height="320" viewBox="0 0 368 320">
        <defs>
          <linearGradient id="houseTones" x1="0" y1="0" x2="0" y2="1">
            <stop offset="0" stop-color="#ffffff"/>
            <stop offset="0.15" stop-color="#7f8a86"/>
            <stop offset="0.45" stop-color="#b9c2bb"/>
            <stop offset="0.62" stop-color="#d8c7a4"/>
            <stop offset="0.75" stop-color="#5d7a3d"/>
            <stop offset="1" stop-color="#4d6a32"/>
          </linearGradient>
        </defs>
        <polygon points="7,13 368,13 368,167 201,240 7,303" fill="url(#houseTones)" role="img" aria-label="Photo of a two-storey house with a wraparound porch on a green lawn"/>
        <polygon points="219,231 368,167 368,303" fill="#111111"/>
      </svg>
      <h2 class="abs tagline"><span class="accent">Make your home</span><span class="dark">fit you!</span></h2>
      <div class="abs contact-mark"></div>
      <div class="abs contact-pill">CONTACT US</div>
      <p class="abs address">NestWell,<br>1480 Harbor Lane NW<br>Tacoma, WA 98402, USA</p>
      <p class="abs phone">CALL US 555.214.7730</p>
      <p class="abs web back-web">www.nestwellsolutions.com</p>
    </section>

    <!-- Cover -->
    <section class="panel panel--cover">
      <div class="abs brand"><span class="brand-name">NestWell</span><span class="brand-square"></span></div>
      <svg class="abs cover-art" width="349" height="415" viewBox="0 0 349 415">
        <defs>
          <linearGradient id="bandPink" x1="0" y1="0" x2="1" y2="0">
            <stop offset="0" stop-color="#c40a6c"/>
            <stop offset="0.5" stop-color="#e0117f"/>
            <stop offset="1" stop-color="#c40a6c"/>
          </linearGradient>
          <linearGradient id="coupleTones" x1="0" y1="0" x2="1" y2="0">
            <stop offset="0" stop-color="#8a4a38"/>
            <stop offset="0.35" stop-color="#c9c4bf"/>
            <stop offset="0.65" stop-color="#6fa6d8"/>
            <stop offset="1" stop-color="#9a5a44"/>
          </linearGradient>
          <linearGradient id="roofFill" x1="0" y1="0" x2="0" y2="1">
            <stop offset="0" stop-color="#ffffff"/>
            <stop offset="1" stop-color="#e6e6e6"/>
          </linearGradient>
        </defs>
        <rect x="0" y="0" width="349" height="145" fill="url(#bandPink)"/>
        <rect x="0" y="133" width="349" height="280" fill="url(#coupleTones)" role="img" aria-label="Photo of a smiling senior couple standing in front of a brick house"/>
        <polygon points="2,140 171,30 347,140 347,118 171,4 2,118" fill="url(#bandPink)"/>
        <polygon points="4,140 171,33 345,140" fill="url(#roofFill)"/>
        <polyline points="0,142 171,30 349,142" fill="none" stroke="#111111" stroke-width="6"/>
        <rect x="0" y="413" width="349" height="2" fill="#ffffff"/>
      </svg>
      <h1 class="abs cover-title"><span class="accent">NestWell</span><span class="light">Solutions</span></h1>
      <div class="footer-band"><p class="web">www.nestwellsolutions.com</p></div>
    </section>

  </div>
</div>
</body>
</html>
```